Job advertisement

A graphic job advertisement. It's supposed to be slightly different from the normal ads. Eye-catcher and later the text for the job description.

```html
<!DOCTYPE html>
<html lang="de">
<head>
<meta charset="utf-8">
<title>Wir suchen SIE! – Power-Worker</title>
<link href="https://fonts.googleapis.com/css2?family=Montserrat:wght@500;800;900&family=Tinos&display=swap" rel="stylesheet">
<style>
  :root {
    --bg: #050508;
    --white: #ffffff;
    --red: #ec1c24;
    --neon-red: #ff2a2a;
    --orange: #f7a400;
    --grey-word: #9c9c9c;
    --brand-grey: #6f7c82;
  }
  html, body {
    margin: 0;
    padding: 0;
    overflow: hidden;
    background: var(--bg);
  }
  .poster {
    position: relative;
    width: 848px;
    height: 1200px;
    overflow: hidden;
    background: var(--bg);
    font-family: "Montserrat", Arial, sans-serif;
  }
  .headline {
    position: absolute;
    margin: 0;
    color: var(--white);
    font-weight: 900;
    line-height: 1;
    white-space: nowrap;
  }
  .headline--search { top: 78px; left: 66px; font-size: 84px; letter-spacing: -2px; }
  .headline--role { top: 184px; left: 74px; font-size: 76px; font-weight: 800; letter-spacing: -2.5px; }

  .brand {
    position: absolute;
    left: 58px;
    top: 322px;
    display: flex;
    flex-direction: column;
    align-items: flex-start;
    gap: 8px;
  }
  .brand__dot {
    width: 30px;
    height: 30px;
    border-radius: 50%;
    background: var(--red);
  }
  .brand__name {
    color: var(--brand-grey);
    font-weight: 500;
    font-size: 26px;
    line-height: 1.05;
  }

  .bulb-visual {
    position: absolute;
    left: 217px;
    top: 321px;
    width: 410px;
    height: 711px;
    border-radius: 205px 205px 110px 110px / 250px 250px 90px 90px;
    background:
      radial-gradient(ellipse at 50% 42%, rgba(247,140,20,0.35) 0%, rgba(80,30,5,0.25) 35%, rgba(0,0,0,0) 60%),
      linear-gradient(180deg, #1b1b1e 0%, #0b0b0d 55%, #3a3a3e 75%, #121214 100%);
  }

  .tagline {
    position: absolute;
    left: 272px;
    top: 585px;
    margin: 0;
    color: var(--orange);
    font-weight: 800;
    font-size: 34px;
    line-height: 1;
    white-space: nowrap;
    transform: rotate(-19.5deg);
    transform-origin: left bottom;
    text-shadow: 0 0 8px rgba(247,164,0,0.7);
  }

  .hiring-badge {
    position: absolute;
    left: 501px;
    top: 298px;
    width: 152px;
    height: 152px;
  }
  .hiring-badge__text {
    position: absolute;
    inset: 0;
    display: flex;
    flex-direction: column;
    align-items: center;
    justify-content: center;
    color: var(--white);
    font-weight: 800;
    font-size: 23px;
    line-height: 1.12;
    transform: rotate(-14deg);
  }

  .unit {
    position: absolute;
    margin: 0;
    color: var(--grey-word);
    font-family: "Tinos", "Times New Roman", serif;
    line-height: 1;
    white-space: nowrap;
  }
  .unit--volt { left: 673px; top: 536px; font-size: 44px; }
  .unit--ohm { left: 119px; top: 714px; font-size: 46px; }
  .unit--voltage { left: 567px; top: 738px; font-size: 42px; }
  .unit--ampere { left: 83px; top: 918px; font-size: 42px; }
  .unit--watt { left: 599px; top: 956px; font-size: 42px; }

  .megaphone {
    position: absolute;
    left: 56px;
    top: 1014px;
    width: 94px;
    height: 84px;
    filter: drop-shadow(0 0 4px var(--neon-red));
  }

  .apply-box {
    position: absolute;
    left: 104px;
    top: 1077px;
    width: 681px;
    height: 54px;
    border: 3px solid var(--neon-red);
    border-radius: 3px;
    box-shadow: 0 0 10px var(--neon-red), inset 0 0 8px rgba(255,42,42,0.6);
    display: flex;
    align-items: center;
  }
  .apply-box__icon {
    margin-left: 18px;
    width: 46px;
    height: 30px;
  }
  .apply-box__text {
    margin: 0 0 0 24px;
    color: var(--white);
    font-weight: 800;
    font-size: 22px;
    white-space: nowrap;
  }
</style>
</head>
<body>
<main class="poster">
  <h1 class="headline headline--search">Wir suchen SIE!</h1>
  <h2 class="headline headline--role">POWER-WORKER</h2>

  <div class="brand">
    <span class="brand__dot"></span>
    <span class="brand__name">elektro<br>vandermeer</span>
  </div>

  <div class="bulb-visual" role="img" aria-label="Photo of a dark light bulb with a glowing orange cable and plug inside"></div>

  <p class="tagline">Wer Suchen Sie!</p>

  <div class="hiring-badge">
    <svg width="152" height="152" viewBox="0 0 152 152" aria-hidden="true">
      <polygon fill="#ec1c24" points="76,0 88,12 104,5 110,21 127,22 126,39 142,46 134,61 148,72 136,84 145,99 130,106 133,123 116,125 112,142 96,137 86,151 74,140 60,150 52,136 35,139 32,123 15,119 20,103 5,94 15,80 3,67 17,57 11,41 28,36 28,19 45,19 51,3 67,10"/>
    </svg>
    <div class="hiring-badge__text"><span>WIR</span><span>STELLEN</span><span>EIN !</span></div>
  </div>

  <p class="unit unit--volt">VOLT</p>
  <p class="unit unit--ohm">Ωhm</p>
  <p class="unit unit--voltage">VOLTAGE</p>
  <p class="unit unit--ampere">AMPERE</p>
  <p class="unit unit--watt">WATT</p>

  <svg class="megaphone" viewBox="0 0 94 84" aria-hidden="true" fill="none" stroke="#ff2a2a" stroke-width="4" stroke-linejoin="round" stroke-linecap="round">
    <path d="M8 50 L20 66 L30 58 L18 42 Z"/>
    <path d="M20 44 L52 12 L70 46 L30 58"/>
    <path d="M58 26 L66 22 L72 32 L66 38"/>
    <path d="M26 62 L36 80 L44 76 L36 60"/>
    <path d="M70 10 L76 2"/>
    <path d="M76 20 L88 16"/>
    <path d="M80 32 L90 34"/>
  </svg>

  <div class="apply-box">
    <svg class="apply-box__icon" viewBox="0 0 46 30" aria-hidden="true">
      <rect x="0" y="0" width="46" height="30" rx="3" fill="#f7a400"/>
      <path d="M3 4 L23 18 L43 4" fill="none" stroke="#7a4a00" stroke-width="2"/>
      <path d="M3 27 L18 15 M43 27 L28 15" fill="none" stroke="#7a4a00" stroke-width="1.5"/>
    </svg>
    <p class="apply-box__text">Bewerbung an : personal@elektrovandermeer.de</p>
  </div>
</main>
</body>
</html>
```